Modern Business Card

Modern professional business card with more than just logo and demographic info. Something memorable.

We are a trendy/modern chiropractic group with an emphasis on neurology, hence the minimalist-type brain logo. We want to convey that modern and technical aspect with professionalism and the elite nature of our practice environment.

```html
<!DOCTYPE html>
<html lang="en">
<head>
<meta charset="utf-8">
<title>Keystone Chiropractic – Business Card</title>
<link rel="stylesheet" href="https://fonts.googleapis.com/css2?family=Crimson+Text:wght@400&family=Roboto:wght@400;500&family=Lato:wght@400&display=swap">
<style>
  :root {
    --page-bg: #ffffff;
    --card-bg: #ffffff;
    --card-edge: #e4e4e4;
    --brand-blue: #4a7fc1;
    --ink-dark: #141414;
    --ink-grey: #5a5a5a;
    --ink-soft: #6b6b6b;
  }
  * { box-sizing: border-box; margin: 0; padding: 0; }
  html, body {
    width: 1200px; height: 1200px; overflow: hidden;
    background: var(--page-bg);
  }
  .canvas { position: relative; width: 1200px; height: 1200px; }

  .card {
    position: absolute;
    left: 232px; width: 703px; height: 407px;
    background: var(--card-bg);
    border: 1px solid var(--card-edge);
  }
  .card--front { top: 173px; border-radius: 0 204px 204px 0; }
  .card--back  { top: 622px; border-radius: 204px 0 0 204px; }

  .wordmark {
    position: absolute;
    font-family: "Crimson Text", Georgia, serif;
    font-weight: 400;
    color: var(--ink-dark);
    line-height: 1;
  }
  .wordmark__top { display: block; }
  .wordmark__bottom { display: block; }

  .card--front .wordmark { left: 45px; top: 46px; }
  .card--front .wordmark__top { font-size: 62px; letter-spacing: 0.5px; }
  .card--front .wordmark__bottom { font-size: 38px; margin-top: 2px; letter-spacing: 0.3px; }

  .brand-disc {
    position: absolute;
    left: 356px; top: 40px;
    width: 320px; height: 320px;
    border-radius: 50%;
    background: var(--brand-blue);
  }

  .person { position: absolute; left: 44px; top: 174px; }
  .person__name {
    font-family: "Roboto", Arial, sans-serif;
    font-weight: 500; font-size: 32px;
    color: var(--brand-blue);
  }
  .person__role {
    font-family: "Roboto", Arial, sans-serif;
    font-size: 20px; color: var(--ink-soft);
    margin-top: 2px;
  }

  .contact-list {
    position: absolute; left: 44px; top: 264px;
    list-style: none;
    font-family: "Lato", Arial, sans-serif;
    font-size: 19px; color: var(--ink-soft);
  }
  .contact-list li {
    display: flex; align-items: center;
    height: 25.7px;
  }
  .contact-list svg { width: 20px; height: 20px; margin-right: 14px; fill: var(--brand-blue); }

  .back-lockup {
    position: absolute; left: 110px; top: 138px;
    display: flex; align-items: center;
  }
  .back-lockup .brand-square {
    width: 128px; height: 128px;
    border-radius: 50%;
    background: var(--brand-blue);
    margin-right: 18px;
  }
  .back-lockup .wordmark { position: static; }
  .back-lockup .wordmark__top { font-size: 62px; }
  .back-lockup .wordmark__bottom { font-size: 40px; margin-top: 2px; }
</style>
</head>
<body>
<main class="canvas">

  <section class="card card--front" aria-label="Card front">
    <h1 class="wordmark">
      <span class="wordmark__top">KEYSTONE</span>
      <span class="wordmark__bottom">CHIROPRACTIC</span>
    </h1>

    <div class="brand-disc" aria-hidden="true"></div>

    <div class="person">
      <p class="person__name">Marlon Reyes</p>
      <p class="person__role">President</p>
    </div>

    <ul class="contact-list">
      <li>
        <svg viewBox="0 0 24 24" aria-hidden="true"><path d="M6.6 10.8a15 15 0 0 0 6.6 6.6l2.2-2.2c.3-.3.7-.4 1-.2 1.1.4 2.3.6 3.6.6.6 0 1 .4 1 1V20c0 .6-.4 1-1 1A17 17 0 0 1 3 4c0-.6.4-1 1-1h3.5c.6 0 1 .4 1 1 0 1.3.2 2.5.6 3.6.1.3 0 .7-.2 1z"/></svg>
        012 3456 7000
      </li>
      <li>
        <svg viewBox="0 0 24 24" aria-hidden="true"><path d="M7 3h10v4H7zM4 8h16a2 2 0 0 1 2 2v6h-4v5H6v-5H2v-6a2 2 0 0 1 2-2zm4 8v3h8v-3z"/></svg>
        012 3456 7001
      </li>
      <li>
        <svg viewBox="0 0 24 24" aria-hidden="true"><path d="M2 5h20v6.5a6 6 0 0 0-9 6.5H2zm2 2v.5l8 5 8-5V7l-8 5zM18 13a5 5 0 1 1 0 10 5 5 0 0 1 0-10zm-2.3 5 1.6 1.6 3-3-.8-.8-2.2 2.2-.8-.8z"/></svg>
        info@keystonechiro.com
      </li>
      <li>
        <svg viewBox="0 0 24 24" aria-hidden="true"><path d="M12 2a10 10 0 1 0 0 20 10 10 0 0 0 0-20zm6.9 6h-3a15 15 0 0 0-1.3-3.9A8 8 0 0 1 18.9 8zM12 4c.8 1.2 1.5 2.5 1.9 4h-3.8c.4-1.5 1.1-2.8 1.9-4zM4.3 14a8 8 0 0 1 0-4h3.4a16 16 0 0 0 0 4zm.8 2h3a15 15 0 0 0 1.3 3.9A8 8 0 0 1 5.1 16zm3-8h-3a8 8 0 0 1 4.3-3.9A15 15 0 0 0 8.1 8zM12 20c-.8-1.2-1.5-2.5-1.9-4h3.8c-.4 1.5-1.1 2.8-1.9 4zm2.3-6H9.7a14 14 0 0 1 0-4h4.6a14 14 0 0 1 0 4zm.3 5.9a15 15 0 0 0 1.3-3.9h3a8 8 0 0 1-4.3 3.9zm1.7-5.9a16 16 0 0 0 0-4h3.4a8 8 0 0 1 0 4z"/></svg>
        www.keystonechiro.com
      </li>
    </ul>
  </section>

  <section class="card card--back" aria-label="Card back">
    <div class="back-lockup">
      <div class="brand-square" aria-hidden="true"></div>
      <h2 class="wordmark">
        <span class="wordmark__top">KEYSTONE</span>
        <span class="wordmark__bottom">CHIROPRACTIC</span>
      </h2>
    </div>
  </section>

</main>
</body>
</html>
```